Tasteful instructions for employees/guests to wash hands

Need an aesthetic visualisation of steps to wash hands.
While we would like to convey the proper steps to wash hands we also don't want to treat our staff/guests like children, rather provide a quick reminder.
Suggested sizes
16″ × 24″
11″ × 14″
A simplified version of these steps:
- Wet your hands with clean, running water (warm or cold), turn off the tap, and apply soap.
- Lather your hands by rubbing them together with the soap. Lather the backs of your hands, between your fingers, and under your nails.
- Scrub your hands for at least 20 seconds.
- Rinse your hands well under clean, running water.
- Dry your hands using a clean towel or air dry them.
Look and feel
Each slider illustrates characteristics of the customer's brand and the style your logo design should communicate.

```html
<!DOCTYPE html>
<html lang="en">
<head>
<meta charset="utf-8">
<title>How to Properly Wash Your Hands</title>
<link rel="stylesheet" href="https://fonts.googleapis.com/css2?family=Bebas+Neue&family=Oswald:wght@200;300&family=Montserrat:wght@400;500;700&display=swap">
<style>
  :root {
    --paper: #f2f3f5;
    --paper-sheen: #fbfbfc;
    --ink: #1b1b1f;
    --ink-soft: #2a2a30;
    --orange: #ef8127;
    --magenta: #b3236a;
    --navy: #12587e;
    --ring-line: #111;
  }
  * { box-sizing: border-box; margin: 0; padding: 0; }
  html, body { width: 900px; height: 1200px; overflow: hidden; }
  body {
    background: var(--paper);
    font-family: "Montserrat", Arial, sans-serif;
    color: var(--ink);
  }
  .poster {
    position: relative;
    width: 900px;
    height: 1200px;
    overflow: hidden;
    background:
      linear-gradient(125deg, transparent 0 18%, var(--paper-sheen) 24%, transparent 32%,
                      transparent 48%, var(--paper-sheen) 56%, transparent 64%,
                      transparent 76%, var(--paper-sheen) 82%, transparent 90%),
      var(--paper);
  }
  .steps-graphic { position: absolute; inset: 0; }
  .title {
    position: absolute;
    inset: 0;
    font-weight: normal;
    pointer-events: none;
  }
  .title span {
    position: absolute;
    display: block;
    line-height: 1;
    white-space: nowrap;
  }
  .title-how {
    left: 64px;
    top: 458px;
    font-family: "Oswald", "Arial Narrow", sans-serif;
    font-weight: 200;
    font-size: 56px;
    color: var(--ink);
    letter-spacing: -1px;
  }
  .title-properly {
    left: 64px;
    top: 517px;
    font-family: "Bebas Neue", "Arial Narrow", sans-serif;
    font-size: 81px;
    color: var(--orange);
  }
  .title-wash {
    left: 62px;
    top: 582px;
    font-family: "Bebas Neue", "Arial Narrow", sans-serif;
    font-size: 177px;
    color: var(--magenta);
    letter-spacing: 1px;
  }
  .title-hands {
    left: 71px;
    top: 751px;
    font-family: "Bebas Neue", "Arial Narrow", sans-serif;
    font-size: 80px;
    color: var(--navy);
  }
  .step { position: absolute; }
  .step h2 {
    font-weight: 700;
    font-size: 19px;
    line-height: 1.3;
    letter-spacing: 0.2px;
    margin-bottom: 12px;
  }
  .step p {
    font-size: 12.5px;
    line-height: 1.45;
    color: var(--ink-soft);
  }
  .step-wet { left: 83px; top: 76px; width: 280px; text-align: center; }
  .step-wet p { font-size: 13px; }
  .step-lather { left: 617px; top: 226px; width: 260px; }
  .step-scrub { left: 698px; top: 610px; width: 180px; }
  .step-rinse { left: 587px; top: 947px; width: 260px; }
  .step-dry { left: 357px; top: 1071px; width: 260px; }
</style>
</head>
<body>
<main class="poster">
  <svg class="steps-graphic" width="900" height="1200" viewBox="0 0 900 1200">
    <defs>
      <linearGradient id="grad-wet" x1="0" y1="0" x2="0" y2="1">
        <stop offset="0" stop-color="#ee62a4"/><stop offset="1" stop-color="#951a4d"/>
      </linearGradient>
      <linearGradient id="grad-lather" x1="0" y1="0" x2="0" y2="1">
        <stop offset="0" stop-color="#8550ae"/><stop offset="1" stop-color="#3b2b82"/>
      </linearGradient>
      <linearGradient id="grad-scrub" x1="0" y1="1" x2="0" y2="0">
        <stop offset="0" stop-color="#5a57a6"/><stop offset="1" stop-color="#7cc6f0"/>
      </linearGradient>
      <linearGradient id="grad-rinse" x1="0" y1="1" x2="0" y2="0">
        <stop offset="0" stop-color="#1d8789"/><stop offset="1" stop-color="#a0d14a"/>
      </linearGradient>
      <linearGradient id="grad-dry" x1="0.2" y1="1" x2="0.8" y2="0">
        <stop offset="0" stop-color="#f06f1e"/><stop offset="1" stop-color="#f6e52a"/>
      </linearGradient>
      <filter id="inner-shadow" x="-30%" y="-30%" width="160%" height="160%">
        <feDropShadow dx="0" dy="3" stdDeviation="5" flood-color="#000" flood-opacity="0.25"/>
      </filter>
    </defs>

    <circle class="step-ring" cx="224" cy="648" r="336" fill="none" stroke="var(--ring-line)" stroke-width="1.6"/>

    <g class="marker marker-wet" transform="translate(222 322)">
      <path d="M0,-142 L70,-70 A99 99 0 1 1 -70,-70 Z" fill="url(#grad-wet)"/>
    </g>
    <g class="marker marker-lather" transform="translate(478 385) rotate(41)">
      <path d="M0,-140 L70,-70 A99 99 0 1 1 -70,-70 Z" fill="url(#grad-lather)"/>
    </g>
    <g class="marker marker-scrub" transform="translate(544 651) rotate(95)">
      <path d="M0,-140 L70,-70 A99 99 0 1 1 -70,-70 Z" fill="url(#grad-scrub)"/>
    </g>
    <g class="marker marker-rinse" transform="translate(456 901) rotate(98)">
      <path d="M0,-140 L70,-70 A99 99 0 1 1 -70,-70 Z" fill="url(#grad-rinse)"/>
    </g>
    <g class="marker marker-dry" transform="translate(208 1005) rotate(129)">
      <path d="M0,-140 L70,-70 A99 99 0 1 1 -70,-70 Z" fill="url(#grad-dry)"/>
    </g>

    <g class="marker-face">
      <circle cx="222" cy="322" r="75" fill="#fff" filter="url(#inner-shadow)"/>
      <circle cx="478" cy="385" r="75" fill="#fff" filter="url(#inner-shadow)"/>
      <circle cx="544" cy="651" r="75" fill="#fff" filter="url(#inner-shadow)"/>
      <circle cx="456" cy="901" r="75" fill="#fff" filter="url(#inner-shadow)"/>
      <circle cx="208" cy="1005" r="75" fill="#fff" filter="url(#inner-shadow)"/>
    </g>

    <g class="step-icon" role="img" aria-label="Line icon: hands held under a running tap">
      <circle cx="222" cy="322" r="42" fill="#f6dde9"/>
    </g>
    <g class="step-icon" role="img" aria-label="Line icon: hand pressing a soap dispenser">
      <circle cx="478" cy="385" r="42" fill="#e4ddf0"/>
    </g>
    <g class="step-icon" role="img" aria-label="Line icon: two hands scrubbing with bubbles">
      <circle cx="544" cy="651" r="42" fill="#e0e4f4"/>
    </g>
    <g class="step-icon" role="img" aria-label="Line icon: hands rinsing under a tap">
      <circle cx="456" cy="901" r="42" fill="#e0f0e2"/>
    </g>
    <g class="step-icon" role="img" aria-label="Line icon: hand under an air dryer">
      <circle cx="208" cy="1005" r="42" fill="#fcebd6"/>
    </g>
  </svg>

  <h1 class="title">
    <span class="title-how">HOW TO</span>
    <span class="title-properly">PROPERLY</span>
    <span class="title-wash">WASH</span>
    <span class="title-hands">YOUR HANDS</span>
  </h1>

  <section class="step step-wet">
    <h2>WET YOUR HANDS</h2>
    <p>with clean, running water (warm or<br>cold), turn off the tap, and apply soap.</p>
  </section>
  <section class="step step-lather">
    <h2>LATHER YOUR HANDS</h2>
    <p>by rubbing them together with the soap. Lather the backs of your hands, between your fingers, and under your nails</p>
  </section>
  <section class="step step-scrub">
    <h2>SCRUB YOUR<br>HANDS</h2>
    <p>for at least 20 seconds.</p>
  </section>
  <section class="step step-rinse">
    <h2>RINSE YOUR HANDS</h2>
    <p>well under clean, running water.</p>
  </section>
  <section class="step step-dry">
    <h2>DRY YOUR HANDS</h2>
    <p>using a clean towel or air dry them.</p>
  </section>
</main>
</body>
</html>
```